KTV Lanternfall

I need a graphic package design for our new bodybuilding sports supplement. The artwork should be clean and useable for many formats. examples or great usage are www.ferrovigorlab.example, www.quartzpulse.example and http://www.belwinnutrition.example/ as examples. I am adding our logo for your reference. The name Lanternfall is because it will help make "Big Guns" as a catch phrase, the product line will have other supplements such as creatine and protein powders and the artwork should be useable on all products. You can see our website for ideas at www.kestovalife.example
Updates

Hi everyone, There are some nice entries coming in. I do wonder if some of you are reading the brief as a few labels don't even highlight the product, KTV is the company, Lanternfall is the Product. Thanks Tam

Industry/Entity Type

Supplement

```html
<!DOCTYPE html>
<html lang="en">
<head>
<meta charset="utf-8">
<title>KTV Lanternfall – Label Design</title>
<link rel="stylesheet" href="https://fonts.googleapis.com/css2?family=Anton&family=Oswald:wght@400;500;600&family=Roboto+Condensed:wght@400;700&display=swap">
<style>
  :root {
    --page-bg: #ffffff;
    --ink: #111111;
    --band-black: #050505;
    --metal-dark: #6e6e6e;
    --metal-mid: #a9a9a9;
    --metal-light: #e4e4e4;
    --leaf-grey: #6a6a6a;
    --accent-red: #ff0000;
    --accent-green: #99ff33;
    --tag-text: #ffffff;
  }
  * { box-sizing: border-box; margin: 0; padding: 0; }
  html, body { width: 1200px; height: 1000px; overflow: hidden; background: var(--page-bg); }
  .canvas { position: relative; width: 1200px; height: 1000px; }

  .label {
    position: absolute;
    top: 160px;
    width: 480px;
    height: 760px;
    border-radius: 18px;
    overflow: hidden;
    background: linear-gradient(90deg, var(--metal-dark) 0%, var(--metal-light) 22%, var(--metal-mid) 48%, var(--metal-dark) 72%, var(--metal-light) 92%, var(--metal-mid) 100%);
  }
  .label--red { left: 75px; --accent: var(--accent-red); }
  .label--green { left: 640px; --accent: var(--accent-green); }

  .ornament-band {
    position: absolute; left: 0; top: 30px; width: 480px; height: 160px;
    background: linear-gradient(180deg, var(--band-black) 0%, var(--band-black) 48%, var(--accent) 58%, var(--accent) 100%);
  }
  .ornament-accent {
    position: absolute; left: 300px; top: 235px; width: 150px; height: 175px;
    border-radius: 10px;
    background: linear-gradient(160deg, var(--leaf-grey) 0%, var(--band-black) 100%);
  }

  .brand { position: absolute; left: 98px; top: 232px; color: var(--ink); font-family: "Oswald", sans-serif; font-weight: 600; }
  .brand__name { font-size: 48px; line-height: 1; letter-spacing: 1px; }
  .brand__company { font-size: 12px; letter-spacing: 1.5px; margin-top: 6px; }

  .product-name { position: absolute; left: 22px; top: 424px; width: 436px; height: 90px; }
  .product-name text { font-family: "Anton", sans-serif; fill: var(--accent); font-size: 94px; }

  .tagline {
    position: absolute; left: 80px; top: 520px; width: 332px; height: 25px;
    background: var(--band-black); color: var(--tag-text);
    font-family: "Oswald", sans-serif; font-weight: 500; font-size: 14px;
    line-height: 25px; text-align: center; letter-spacing: 0.3px;
  }

  .benefits { position: absolute; left: 82px; top: 566px; list-style: none; font-family: "Roboto Condensed", sans-serif; font-size: 11.5px; color: var(--ink); }
  .benefits li { position: relative; padding-left: 20px; height: 21px; line-height: 21px; }
  .benefits li::before {
    content: ""; position: absolute; left: 2px; top: 8px; width: 11px; height: 4px;
    background: var(--accent); border-radius: 2px 0 2px 0; transform: rotate(-30deg);
  }

  .claim { position: absolute; left: 0; width: 480px; text-align: center; font-family: "Roboto Condensed", sans-serif; }
  .claim--study { top: 664px; font-size: 15px; color: var(--ink); }
  .claim--category { top: 694px; font-size: 19px; color: var(--accent); font-family: "Oswald", sans-serif; font-weight: 400; letter-spacing: 0.4px; }
</style>
</head>
<body>
<main class="canvas">

  <section class="label label--red" aria-label="KTV Lanternfall label, red variant">
    <div class="ornament-band" role="img" aria-label="Decorative sweeping band in black and red"></div>
    <div class="ornament-accent" role="img" aria-label="Decorative leaf-shaped accent in grey and black"></div>
    <div class="brand">
      <div class="brand__name">KTV</div>
      <div class="brand__company">KESTOVA LIFE SCIENCE</div>
    </div>
    <svg class="product-name" viewBox="0 0 436 90" aria-label="Lanternfall">
      <text x="0" y="88" textLength="436" lengthAdjust="spacingAndGlyphs">LANTERNFALL</text>
    </svg>
    <div class="tagline">THE FIRST CHEWABLE STRENGTH ENHANCER</div>
    <ul class="benefits">
      <li>Increase Protein Synthesis while Reducing Protein Breakdown</li>
      <li>Increased Muscle Mass, Strength and Endurance</li>
      <li>Reduce Muscle Fatigue and Increase Blood Flow</li>
      <li>Increase Joint Range of Motion &amp; Decrease Joint Discomfort</li>
    </ul>
    <p class="claim claim--study">Clinically Studied Formula</p>
    <p class="claim claim--category">DIETARY SUPPLEMENTS</p>
  </section>

  <section class="label label--green" aria-label="KTV Lanternfall label, green variant">
    <div class="ornament-band" role="img" aria-label="Decorative sweeping band in black and green"></div>
    <div class="ornament-accent" role="img" aria-label="Decorative leaf-shaped accent in grey and black"></div>
    <div class="brand">
      <div class="brand__name">KTV</div>
      <div class="brand__company">KESTOVA LIFE SCIENCE</div>
    </div>
    <svg class="product-name" viewBox="0 0 436 90" aria-label="Lanternfall">
      <text x="0" y="88" textLength="436" lengthAdjust="spacingAndGlyphs">LANTERNFALL</text>
    </svg>
    <div class="tagline">THE FIRST CHEWABLE STRENGTH ENHANCER</div>
    <ul class="benefits">
      <li>Increase Protein Synthesis while Reducing Protein Breakdown</li>
      <li>Increased Muscle Mass, Strength and Endurance</li>
      <li>Reduce Muscle Fatigue and Increase Blood Flow</li>
      <li>Increase Joint Range of Motion &amp; Decrease Joint Discomfort</li>
    </ul>
    <p class="claim claim--study">Clinically Studied Formula</p>
    <p class="claim claim--category">DIETARY SUPPLEMENTS</p>
  </section>

</main>
</body>
</html>
```